Two Industrial Businesses in Need of One Cohesive Design

We have two businesses under the same ownership that do different types of work and we are working to make the two brands work better together. Therefore, we would like to develop a single business card that works for both companies. I have two basic schools of the thought on how this could work One is that each side of the card could be dedicated to one business. In this scenario each side could have its own branding, colors, etc. and would also include name, title and contact info. The other option would be to create a design and that works well with both logos on one side of the card and then on the other side include the name, title and contact information.

I would like the card to be a modern and professional design. Some of our customers are large industrial equipment manufacturers like Borvane, Hal Pettik and various heavy duty trucking companies so the card should have an industrial look. For some branding inspiration and a little more info about what we do please refer to our websites.

www.finishcoatworks.example
www.tolvecooling.example/v3/ (This is our new and unfinished site, but you can see the branding we are trying to achieve)

I have attached our two logos as well as the cover page to a recent printed line card that may help give you an idea of what I mean by an industrial look although I don't want that much color on the business card.

Target Market(s)

Commercial Trucking Companies, Industrial Equipment Manufacturers, Metal Fabrication Companies, Individual Customers, Ag Farmers

Industry/Entity Type

Industrial

Contact Information for Business Card

Company 1: Tolve Cooling Inc.
Company 2: Finish Coat Works
Name: Corwin Hadley
Title: Operations Manager
Phone for Company 1: 555 214 3780
Phone for Company 2: 555 617 2093
Email for Company 1: corwin@tolvecooling.example
Email for Company 2: corwin @finishcoatworks.example
Website for Company 1: www.tolvecooling.example
Website for Company 2: www.finishcoatworks.example
Physical Address: 482 Marlow St, Bloomington, IL 61799

Font styles to use
Sans Serif

Requirements
Must have
• - Include both logos
• - Combination of industrial and modern design - I have attached a few designs that I like.
• - When choosing colors for the design, try to use colors that go well with or match the colors in the logos.
Nice to have
• I like when designers use two colors on the name. For example, the person's first name is one color and the person's last name is another.
• I like designs that incorporate "icons" near the contact details. For example, near the phone numbers there could be a phone icon.
Should not have
• If we put one logo on each side the card should not have too much color. They should try to maintain a combination of an industrial and modern look.

```html
<!DOCTYPE html>
<html lang="en">
<head>
<meta charset="utf-8">
<title>Corwin Hadley – Business Cards</title>
<link rel="stylesheet" href="https://fonts.googleapis.com/css2?family=Open+Sans:wght@400;600;700&display=swap">
<style>
  :root {
    --backdrop: #d4d4d4;
    --card-white: #f4f5f7;
    --card-black: #1b1b1b;
    --ink: #1e1e1e;
    --ink-soft: #2c2c2c;
    --tolve-red: #d3202f;
    --finish-yellow: #f2c200;
    --logo-white: #ffffff;
  }
  * { box-sizing: border-box; margin: 0; padding: 0; }
  html, body {
    width: 1200px; height: 900px; overflow: hidden;
    background: var(--backdrop);
    font-family: "Open Sans", Arial, sans-serif;
    color: var(--ink);
  }
  .sheet {
    width: 1200px; height: 900px;
    display: flex; align-items: center; justify-content: center; gap: 50px;
  }
  .card {
    width: 525px; height: 300px;
    display: flex;
    background: var(--card-white);
    box-shadow: 0 6px 18px rgba(0,0,0,0.18);
  }
  .card--tolve { --accent: var(--tolve-red); }
  .card--finish { --accent: var(--finish-yellow); }

  .brand-panel {
    width: 44%;
    background: var(--card-black);
    display: flex; align-items: flex-end; justify-content: center;
    padding: 0 18px 40px;
  }
  .brand-mark {
    display: flex; align-items: center; gap: 8px;
    color: var(--logo-white);
    font-weight: 700; font-size: 19px; line-height: 1.1;
    text-transform: uppercase; letter-spacing: 0.5px;
  }
  .brand-mark__dot {
    width: 12px; height: 12px; border-radius: 50%;
    background: var(--logo-white); flex: none;
  }

  .details {
    flex: 1;
    padding: 34px 16px 20px 22px;
    display: flex; flex-direction: column;
  }
  .person__name {
    font-size: 24px; font-weight: 700; line-height: 1.1;
    color: var(--ink);
  }
  .person__name .accent { color: var(--accent); }
  .person__title {
    font-size: 15px; font-weight: 400; color: var(--ink-soft);
    margin-bottom: 18px;
  }
  .contact-group { list-style: none; margin-bottom: 14px; }
  .contact-group li {
    display: flex; align-items: flex-start; gap: 9px;
    font-size: 12.5px; line-height: 1.5; color: var(--ink-soft);
  }
  .contact-group svg {
    width: 13px; height: 13px; flex: none; margin-top: 3px;
    fill: var(--accent);
  }
  .contact-group .outline { fill: none; stroke: var(--accent); stroke-width: 2; }
  .web strong { font-weight: 700; }
</style>
</head>
<body>
<main class="sheet">

  <article class="card card--tolve">
    <div class="brand-panel">
      <div class="brand-mark"><span class="brand-mark__dot"></span>Tolve Cooling Inc.</div>
    </div>
    <div class="details">
      <h1 class="person__name">Corwin <span class="accent">Hadley</span></h1>
      <p class="person__title">Operations Manager</p>
      <ul class="contact-group">
        <li><svg viewBox="0 0 16 16"><rect class="outline" x="3" y="1" width="10" height="14" rx="1.5"/></svg>xxx xxx xxxx</li>
        <li><svg viewBox="0 0 16 16"><path d="M1 5c2-3 12-3 14 0l-2 2-3-1V4H6v2L3 7zM3 9h10v5H3zM6 10.5h4v2H6z"/></svg>555 214 3780</li>
      </ul>
      <ul class="contact-group">
        <li><svg viewBox="0 0 16 16"><path d="M1 3h14v2L8 9 1 5zM1 7l7 4 7-4v6H1z"/></svg>corwin@tolvecooling.example</li>
        <li><svg viewBox="0 0 16 16"><path class="outline" d="M7 9l2-2M6 6L4 8a2.5 2.5 0 0 0 4 4l2-2M10 10l2-2a2.5 2.5 0 0 0-4-4L6 6"/></svg>www.tolvecooling.example</li>
        <li><svg viewBox="0 0 16 16"><path d="M8 1a5 5 0 0 1 5 5c0 4-5 9-5 9S3 10 3 6a5 5 0 0 1 5-5zm0 3a2 2 0 1 0 0 4 2 2 0 0 0 0-4z"/></svg>482 Marlow St, Bloomington,<br>IL 61799</li>
      </ul>
    </div>
  </article>

  <article class="card card--finish">
    <div class="brand-panel">
      <div class="brand-mark"><span class="brand-mark__dot"></span>Finish Coat Works</div>
    </div>
    <div class="details">
      <h1 class="person__name"><span class="accent">Corwin</span> Hadley</h1>
      <p class="person__title">Operations Manager</p>
      <ul class="contact-group">
        <li><svg viewBox="0 0 16 16"><rect class="outline" x="3" y="1" width="10" height="14" rx="1.5"/></svg>xxx xxx xxxx</li>
        <li><svg viewBox="0 0 16 16"><path d="M1 5c2-3 12-3 14 0l-2 2-3-1V4H6v2L3 7zM3 9h10v5H3zM6 10.5h4v2H6z"/></svg>555 617 2093</li>
      </ul>
      <ul class="contact-group">
        <li><svg viewBox="0 0 16 16"><path d="M1 3h14v2L8 9 1 5zM1 7l7 4 7-4v6H1z"/></svg>corwin@finishcoatworks.example</li>
        <li class="web"><svg viewBox="0 0 16 16"><path class="outline" d="M7 9l2-2M6 6L4 8a2.5 2.5 0 0 0 4 4l2-2M10 10l2-2a2.5 2.5 0 0 0-4-4L6 6"/></svg><span>www.<strong>finishcoat</strong>works.example</span></li>
        <li><svg viewBox="0 0 16 16"><path d="M8 1a5 5 0 0 1 5 5c0 4-5 9-5 9S3 10 3 6a5 5 0 0 1 5-5zm0 3a2 2 0 1 0 0 4 2 2 0 0 0 0-4z"/></svg>482 Marlow St, Bloomington,<br>IL 61799</li>
      </ul>
    </div>
  </article>

</main>
</body>
</html>
```